Animal Horse & Bedding Company Needs a Website Coded & Designed

We need a website for a new animal bedding and feed company that is visually grabbing and vibrant. We would like to see a website that displays trust, quality and confidence. Needs to be responsive and mobile friendly for all browsers and coded for both Android & IOS. SEO is also important.

Joomla or Wordpress – must be both desktop and mobile friendly with fast page load speed. Need the ability to edit ourselves in Wordpress or Joomla.

Full details attached below with some layout and content ideas.

Coding

Coded - Design and coding required

Number of Pages Required

5+ page

Font styles to use
Sans Serif

Requirements
Must have
• Needs to be responsive and mobile friendly for all browsers and coded for both Android & IOS. SEO is also important.

Wordpress – must be both desktop and mobile friendly with fast page load speed. Need the ability to edit ourselves in Wordpress.

Logo Colours:
Dark Brown
CMYK: 50 / 70 / 80 / 70
Pantone: 4625C

Orange
CMYK: 0 / 50 / 100 / 0
Pantone: 144C
Nice to have
• Use picture of building attached and super impose logo on building.

```html
<!DOCTYPE html>
<html lang="en">
<head>
<meta charset="utf-8">
<title>Golden Sheaf — Bedding &amp; Feed</title>
<link href="https://fonts.googleapis.com/css2?family=Oswald:wght@300;400;500&family=Montserrat:wght@400;500;600;700&display=swap" rel="stylesheet">
<style>
:root{
  --brown:#3d2314;
  --brown-soft:#5a3a26;
  --orange:#f7941d;
  --cream:#f9f5ef;
  --white:#ffffff;
  --text:#3a2a20;
  --muted:#6b5a4e;
  --line:#ddd3c8;
}
*{margin:0;padding:0;box-sizing:border-box}
html,body{width:1200px;height:3463px;overflow:hidden}
body{position:relative;background:var(--white);font-family:"Montserrat",sans-serif;color:var(--text)}
.abs{position:absolute}
.display{font-family:"Oswald",sans-serif;font-weight:400;color:var(--brown);text-transform:uppercase}

/* header */
.site-header{left:0;top:0;width:1200px;height:95px;background:var(--white);z-index:5}
.brand{left:72px;top:16px;display:flex;align-items:center;gap:12px}
.brand-dot{width:44px;height:44px;border-radius:50%;border:3px solid var(--orange)}
.brand-name{font-family:"Oswald",sans-serif;font-weight:400;font-size:32px;letter-spacing:2px;color:var(--brown);line-height:1}
.brand-sub{display:block;font-size:12px;letter-spacing:9px;margin-top:4px}
.nav a{position:absolute;top:34px;font-size:14px;color:var(--brown);text-decoration:none;font-weight:500}
.nav a.active{font-weight:700}
.nav a.active::after{content:"";position:absolute;left:8px;right:8px;bottom:-16px;height:2px;background:var(--orange)}
.btn{display:flex;align-items:center;justify-content:center;gap:8px;background:var(--brown);color:var(--white);font-weight:700;font-size:13px;text-transform:uppercase;text-decoration:none}
.btn-quote{left:962px;top:27px;width:154px;height:38px;border-radius:20px;font-size:12px}

/* hero */
.hero{left:0;top:95px;width:1200px;height:650px;background:linear-gradient(180deg,#6b7a3a 0%,#8a7a3c 45%,#a77b42 75%,#c9a46a 100%)}
.hero-horse{left:560px;top:100px;width:560px;height:560px;background:radial-gradient(ellipse at center,#9a4a1c 0%,rgba(154,74,28,.6) 45%,rgba(154,74,28,0) 70%)}
.hero-title{left:64px;top:290px;font-family:"Oswald",sans-serif;font-size:88px;font-weight:400;color:var(--white);letter-spacing:2px;line-height:1}
.hero-sub{left:158px;top:385px;font-family:"Oswald",sans-serif;font-size:36px;letter-spacing:12px;color:var(--white)}
.btn-learn{left:214px;top:443px;width:182px;height:50px;border-radius:22px 0 22px 0;font-size:14px;box-shadow:4px 4px 0 #d9b98a}
.hero-curve{left:0;top:620px;width:1200px;height:130px}
.dots{left:571px;top:667px;display:flex;gap:9px}
.dots span{width:11px;height:11px;border-radius:50%;background:var(--white);border:2px solid var(--white)}
.dots span.on{background:transparent}

/* cards */
.card{top:790px;width:320px;height:407px;background:var(--white);box-shadow:0 0 8px rgba(0,0,0,.12);text-align:center}
.card.dark{background:var(--brown)}
.card-photo{height:210px}
.card h3{font-family:"Oswald",sans-serif;font-weight:400;font-size:25px;color:var(--brown);margin-top:24px}
.card.dark h3{color:var(--white)}
.card .rule{width:34px;height:2px;background:var(--orange);margin:8px auto 18px}
.card p{font-size:10.5px;line-height:14px;color:var(--muted);padding:0 42px}
.card.dark p{color:#eadfd3}

/* features */
.features{left:0;top:1251px;width:1200px;height:238px;background:var(--cream);border-bottom:1px solid var(--line)}
.feature h4{font-size:17px;font-weight:500;color:var(--brown);line-height:21px;text-transform:uppercase;letter-spacing:.5px}
.feature p{font-size:11px;line-height:19px;color:var(--muted);margin-top:8px}
.divider{width:1px;height:110px;background:var(--line);top:1345px}

/* bedding */
.section-title{font-family:"Oswald",sans-serif;font-weight:400;font-size:44px;color:var(--brown);text-align:center;line-height:1}
.title-rule{width:56px;height:2px;background:var(--orange)}
.bed-photo{left:421px;top:1656px;width:360px;height:360px;border-radius:50%;background:radial-gradient(circle at 50% 45%,#a65a26 0%,#8d6a3e 45%,#b8a27a 75%,#d8cfbd 100%)}
.ico{width:76px;height:76px;border-radius:50%;display:flex;align-items:center;justify-content:center}
.ico.o{background:var(--orange)}
.ico.d{background:var(--brown)}
.label{font-size:14.5px;line-height:19px;color:var(--brown)}
.label.r{text-align:right}
.btn-bed{left:505px;top:2261px;width:189px;height:52px;border-radius:22px 0 22px 0;font-size:14px}
.arrows{left:360px;top:1690px;width:480px;height:380px}

/* feed */
.feed{left:0;top:2403px;width:1200px;height:700px;background:var(--cream)}
.feed-text{left:120px;top:2558px;width:520px;font-size:12.5px;line-height:20px;color:var(--brown)}
.perk{display:flex;align-items:center;gap:8px;font-size:10.5px;font-weight:700;color:var(--brown);line-height:12px}
.btn-feed{left:122px;top:2868px;width:155px;height:48px;border-radius:22px 0 0 0;font-size:13px}
.feed-photo{left:695px;top:2491px;width:404px;height:342px;background:linear-gradient(135deg,#7d8790 0%,#8a5a36 40%,#b48a62 70%,#e0d6cb 100%)}
.feed-frame{left:603px;top:2712px;width:254px;height:213px;background:var(--orange)}
.feed-pellets{left:620px;top:2720px;width:220px;height:186px;background:radial-gradient(circle at 40% 40%,#c99a58 0%,#8e6532 60%,#5e3f1d 100%)}

/* footer */
.footer{left:0;top:2975px;width:1200px;height:488px;background:var(--brown)}
.footer-curve{left:0;top:2970px;width:1200px;height:110px}
.f-brand{left:120px;top:3160px;text-align:center;width:230px}
.f-brand .brand-name{color:var(--white);font-size:38px}
.f-brand .brand-sub{color:var(--orange);font-size:13px;letter-spacing:10px}
.f-mark{left:215px;top:3108px;width:40px;height:40px;border-radius:50%;border:3px solid var(--orange)}
.social{left:158px;top:3256px;display:flex;gap:8px}
.social span{width:30px;height:30px;border-radius:50%;background:var(--white)}
.social span:first-child{background:var(--orange)}
.f-head{font-size:14px;font-weight:500;color:var(--white);text-transform:uppercase}
.f-links a{display:block;font-size:11px;color:#eadfd3;text-decoration:none;line-height:26px}
.f-contact{font-size:10px;color:#eadfd3;line-height:26px}
.f-contact div{display:flex;align-items:center;gap:10px}
.news-input{left:859px;top:3170px;width:230px;height:35px;border:1px solid #a89282;border-radius:18px;font-size:10px;color:#d8c9bb;padding:11px 20px}
.btn-sub{left:864px;top:3220px;width:131px;height:35px;border-radius:18px;background:var(--white);color:var(--brown);font-size:11px}
.copyright{left:0;top:3387px;width:1200px;text-align:center;font-size:10px;color:#cdbcae}
</style>
</head>
<body>

<header class="abs site-header">
  <div class="abs brand">
    <span class="brand-dot"></span>
    <div class="brand-name">GOLDEN SHEAF<span class="brand-sub">BEDDING &amp; FEED</span></div>
  </div>
  <nav class="nav">
    <a class="active" href="#" style="left:412px">HOME</a>
    <a href="#" style="left:509px">ABOUT</a>
    <a href="#" style="left:612px">FEED</a>
    <a href="#" style="left:700px">BEDDING</a>
    <a href="#" style="left:818px">CONTACT US</a>
  </nav>
  <a class="abs btn btn-quote" href="#">Request Quote ›</a>
</header>

<section class="abs hero" role="img" aria-label="Chestnut horse standing in a summer meadow with trees behind"></section>
<div class="abs hero-horse"></div>
<h1 class="abs hero-title">GOLDEN SHEAF</h1>
<div class="abs hero-sub">BEDDING &amp; FEED</div>
<a class="abs btn btn-learn" href="#">Learn More ›</a>
<svg class="abs hero-curve" viewBox="0 0 1200 130" preserveAspectRatio="none">
  <path d="M0 20 Q600 150 1200 20 L1200 130 L0 130 Z" fill="#ffffff"/>
  <path d="M0 20 Q600 150 1200 20 L1200 130 L0 130 Z" fill="#f9f5ef" opacity=".5"/>
  <path d="M0 30 Q600 150 1200 30" fill="none" stroke="#f7941d" stroke-width="5"/>
  <path d="M0 130 L0 40 Q600 158 1200 40 L1200 130 Z" fill="#ffffff"/>
</svg>
<div class="abs dots"><span></span><span class="on"></span><span></span></div>

<article class="abs card" style="left:108px">
  <div class="card-photo" role="img" aria-label="Two horses eating hay together" style="background:linear-gradient(160deg,#9aa6b4,#3a2a22 55%,#c9b27a)"></div>
  <h3>BEST BEDDING &amp; FEED</h3><div class="rule"></div>
  <p>Looking for the best bedding and feed for your horse, livestock or household pet look no further. We use premium locally sourced straw and hay in all of our products and are committed in providing quality products and service.</p>
</article>
<article class="abs card dark" style="left:445px">
  <div class="card-photo" role="img" aria-label="Woman with a horse outdoors among green leaves" style="background:linear-gradient(120deg,#7a4a24,#8aa23c 55%,#c8b24a)"></div>
  <h3>ANIMAL DESERVE BEST</h3><div class="rule"></div>
  <p>Your animal deserves the very best in health and comfort to keep them healthy, strong and happy. Our products are designed for horses, livestock (goats, cattle and sheep), small caged animals (rabbits, guinea pigs and more).</p>
</article>
<article class="abs card" style="left:781px">
  <div class="card-photo" role="img" aria-label="Chestnut pony in a green field" style="background:linear-gradient(180deg,#b9d4e6,#d8d7a0 45%,#9a6a2c 70%,#7c9a2e)"></div>
  <h3>OFFER SUPPLY &amp; DELIVERY</h3><div class="rule"></div>
  <p>The Golden Sheaf offers supply and delivery of fresh bedding as well as removal of waste bedding. Let us deliver you a container of fresh straw and haul your waste bedding away. A full service solution that is sustainable and responsible.</p>
</article>

<section class="abs features">
  <div class="abs feature" style="left:112px;top:80px;display:flex;gap:10px">
    <svg width="44" height="66" viewBox="0 0 44 66" fill="none" stroke="#f7941d" stroke-width="2"><circle cx="22" cy="22" r="20"/><circle cx="22" cy="22" r="13"/><path d="M12 38 L6 62 L14 56 L18 64 L22 44 L26 64 L30 56 L38 62 L32 38"/></svg>
    <div><h4>Quality<br>Guaranteed</h4><p>Grown for quality - 100% natural with no<br>chemicals or additives</p></div>
  </div>
  <div class="abs feature" style="left:460px;top:80px;display:flex;gap:12px">
    <svg width="50" height="54" viewBox="0 0 50 54" fill="none" stroke="#f7941d" stroke-width="3"><path d="M10 12 A22 22 0 1 0 40 12"/><path d="M16 16 L34 38 M34 16 L16 38"/></svg>
    <div><h4>Full Service<br>Solution</h4><p>Dedicated in providing a full service solution<br>of bedding supply &amp; waste removal</p></div>
  </div>
  <div class="abs feature" style="left:820px;top:80px;display:flex;gap:12px">
    <svg width="60" height="62" viewBox="0 0 60 62" fill="none" stroke="#f7941d" stroke-width="2"><ellipse cx="30" cy="38" rx="26" ry="19"/><circle cx="38" cy="12" r="8"/><path d="M16 55 v6 M40 55 v6"/></svg>
    <div><h4>Convenient &amp; Cost<br>Effective</h4><p>Compressed bags , pellets or bulk products<br>saving in shipping costs</p></div>
  </div>
</section>
<div class="abs divider" style="left:430px"></div>
<div class="abs divider" style="left:800px"></div>

<h2 class="abs section-title" style="left:0;top:1570px;width:1200px">BEDDING</h2>
<div class="abs title-rule" style="left:572px;top:1624px"></div>

<div class="abs bed-photo" role="img" aria-label="Horse lying down on a bed of straw"></div>
<svg class="abs arrows" viewBox="0 0 480 380" fill="none" stroke="#9c9c9c" stroke-width="2">
  <path d="M85 50 Q60 20 28 18 M28 18 l8 -7 M28 18 l8 7"/>
  <path d="M400 50 Q420 20 455 18 M455 18 l-8 -7 M455 18 l-8 7"/>
  <path d="M72 210 Q55 240 12 238 M12 238 l9 -6 M12 238 l8 8"/>
  <path d="M412 210 Q430 240 472 238 M472 238 l-9 -6 M472 238 l-8 8"/>
  <path d="M148 310 Q125 336 86 335 M86 335 l9 -6 M86 335 l8 8"/>
  <path d="M315 318 Q335 340 380 336 M380 336 l-9 -6 M380 336 l-8 8"/>
  <path d="M240 334 V 378 M240 378 l-7 -9 M240 378 l7 -9"/>
</svg>

<div class="abs ico o" style="left:283px;top:1674px"><svg width="34" height="40" viewBox="0 0 34 40" fill="none" stroke="#fff" stroke-width="2"><path d="M17 2 C30 14 30 28 17 36 C4 28 4 14 17 2 Z M17 8 V39 M17 18 l-6 -5 M17 18 l6 -5 M17 26 l-7 -5 M17 26 l7 -5"/></svg></div>
<div class="abs label r" style="left:120px;top:1691px;width:148px">100% Natural<br>Chopped Straw</div>

<div class="abs ico d" style="left:301px;top:1849px"><svg width="46" height="46" viewBox="0 0 46 46" fill="none" stroke="#fff" stroke-width="2"><circle cx="23" cy="23" r="20"/><circle cx="23" cy="23" r="11"/><path d="M9 9 L37 37"/></svg></div>
<div class="abs label r" style="left:190px;top:1876px;width:96px">Low Dust</div>

<div class="abs ico o" style="left:365px;top:2019px"><svg width="40" height="40" viewBox="0 0 40 40" fill="none" stroke="#fff" stroke-width="2"><circle cx="20" cy="20" r="18"/><path d="M16 8 h8 M18 8 v8 L10 30 h20 L22 16 v-8"/></svg></div>
<div class="abs label r" style="left:215px;top:2036px;width:137px">Chemical &amp;<br>Additive Free</div>

<div class="abs ico d" style="left:562px;top:2097px"><svg width="42" height="42" viewBox="0 0 42 42" fill="none" stroke="#fff" stroke-width="2"><circle cx="10" cy="28" r="6"/><circle cx="26" cy="30" r="7"/><circle cx="18" cy="14" r="5"/><path d="M32 6 v8 M28 10 h8"/></svg></div>
<div class="abs label" style="left:500px;top:2184px;width:204px;text-align:center">Clean &amp; Highly<br>Absorbent</div>

<div class="abs ico o" style="left:752px;top:2019px"><svg width="46" height="30" viewBox="0 0 46 30" fill="none" stroke="#fff" stroke-width="2"><path d="M2 26 h42 M6 26 L12 14 h22 l6 12 M16 14 L20 4 h8 l2 10"/></svg></div>
<div class="abs label" style="left:839px;top:2036px;width:150px">Cheaper than<br>Wood Shavings</div>

<div class="abs ico d" style="left:817px;top:1849px"><svg width="44" height="44" viewBox="0 0 44 44" fill="none" stroke="#fff" stroke-width="2"><circle cx="22" cy="22" r="19"/><path d="M8 16 q8 -4 12 4 q4 8 -4 12 M26 6 q-2 8 8 10 q6 2 6 10"/></svg></div>
<div class="abs label" style="left:905px;top:1871px;width:170px">Economic – less used<br>and less wasted</div>

<div class="abs ico o" style="left:843px;top:1674px"><svg width="44" height="42" viewBox="0 0 44 42" fill="none" stroke="#fff" stroke-width="2"><path d="M22 4 L32 20 M22 4 L12 20 M6 28 L14 40 H30 M38 28 L30 40 M12 20 L6 28 M32 20 L38 28"/></svg></div>
<div class="abs label" style="left:934px;top:1693px;width:200px">Environmentally Friendly –<br>Recyclable &amp; Compostable</div>

<a class="abs btn btn-bed" href="#">View Bedding ›</a>

<section class="abs feed"></section>
<h2 class="abs section-title" style="left:118px;top:2495px">OUR FEED</h2>
<p class="abs feed-text">Hay cubes and pellets are made from premium hay offering a variety of animals a feed that is non-GMO and packed with natural nutrients.&nbsp; These pellets and cubes are less bulky to handle, store and ship. As well, they reduce the amount of wasted feed.</p>

<div class="abs perk" style="left:120px;top:2655px"><svg width="24" height="32" viewBox="0 0 24 32" fill="none" stroke="#f7941d" stroke-width="1.6"><path d="M12 2 C22 12 22 22 12 29 C2 22 2 12 12 2 Z M12 6 V31"/></svg>100% Natural</div>
<div class="abs perk" style="left:292px;top:2655px"><svg width="32" height="32" viewBox="0 0 32 32" fill="none" stroke="#f7941d" stroke-width="1.6"><circle cx="16" cy="16" r="14"/><path d="M13 6 h6 M14 6 v6 L8 24 h16 L18 12 V6"/></svg>Chemical &amp;<br>Additive Free</div>
<div class="abs perk" style="left:443px;top:2655px"><svg width="36" height="32" viewBox="0 0 36 32" fill="none" stroke="#f7941d" stroke-width="1.6"><path d="M18 2 l8 4 v8 l-8 4 l-8 -4 v-8 Z M4 16 l8 4 v8 l-8 -4 Z M32 16 l-8 4 v8 l8 -4 Z"/></svg>Available in<br>Pellets or Cubes</div>

<div class="abs perk" style="left:115px;top:2730px"><svg width="34" height="34" viewBox="0 0 34 34" fill="none" stroke="#f7941d" stroke-width="1.6"><circle cx="8" cy="24" r="6"/><circle cx="22" cy="26" r="5"/><circle cx="14" cy="10" r="5"/><path d="M28 4 v8 M24 8 h8"/></svg>Clean - Eliminates<br>Dust From Feeding<br>Baled Hay</div>
<div class="abs perk" style="left:292px;top:2728px"><svg width="32" height="36" viewBox="0 0 32 36" fill="none" stroke="#f7941d" stroke-width="1.6"><path d="M4 6 h24 M12 6 V2 h8 v4 M7 6 l3 28 h12 l3 -28 M13 12 v16 M19 12 v16"/></svg>Eliminate Waste<br>In Feeding</div>
<div class="abs perk" style="left:447px;top:2730px"><svg width="32" height="30" viewBox="0 0 32 30" fill="none" stroke="#f7941d" stroke-width="1.6"><path d="M2 20 q6 -12 12 -2 q6 10 14 -8 M4 26 q6 -12 12 -2 q6 10 14 -8"/></svg>High Protein<br>Content</div>

<div class="abs perk" style="left:112px;top:2800px"><svg width="36" height="34" viewBox="0 0 36 34" fill="none" stroke="#f7941d" stroke-width="1.6"><circle cx="16" cy="17" r="14"/><path d="M20 11 h-6 a3 3 0 0 0 0 6 h4 a3 3 0 0 1 0 6 h-6 M16 8 v18"/></svg>Cost Effective</div>
<div class="abs perk" style="left:288px;top:2800px"><svg width="38" height="36" viewBox="0 0 38 36" fill="none" stroke="#f7941d" stroke-width="2"><path d="M30 10 A15 15 0 1 1 22 3"/><path d="M10 18 l7 7 L36 4"/></svg>Convenient</div>
<div class="abs perk" style="left:447px;top:2800px"><svg width="34" height="32" viewBox="0 0 34 32" fill="none" stroke="#f7941d" stroke-width="1.6"><path d="M17 2 l8 4 v8 l-8 4 l-8 -4 v-8 Z M3 16 l8 4 v8 l-8 -4 Z M31 16 l-8 4 v8 l8 -4 Z"/></svg>Less wasted<br>feed</div>

<a class="abs btn btn-feed" href="#">View Feed</a>

<div class="abs feed-photo" role="img" aria-label="Farmer feeding a horse from a bucket at a fence"></div>
<div class="abs feed-frame"></div>
<div class="abs feed-pellets" role="img" aria-label="Close view of hay feed pellets"></div>

<footer class="abs footer"></footer>
<svg class="abs footer-curve" viewBox="0 0 1200 110" preserveAspectRatio="none"><path d="M0 0 H1200 V5 Q600 210 0 5 Z" fill="#f9f5ef"/></svg>

<div class="abs f-mark"></div>
<div class="abs f-brand"><div class="brand-name">GOLDEN SHEAF<span class="brand-sub">BEDDING &amp; FEED</span></div></div>
<div class="abs social"><span></span><span></span><span></span><span></span></div>

<div class="abs f-head" style="left:421px;top:3135px">Sitemap</div>
<nav class="abs f-links" style="left:421px;top:3168px">
  <a href="#">Home</a><a href="#">About Us</a><a href="#">Our Bedding</a><a href="#">Feed</a><a href="#">Contact Us</a>
</nav>

<div class="abs f-head" style="left:596px;top:3136px">Contact Us</div>
<div class="abs f-contact" style="left:596px;top:3166px">
  <div><svg width="14" height="18" viewBox="0 0 14 18"><path d="M7 0 a7 7 0 0 1 7 7 c0 5 -7 11 -7 11 S0 12 0 7 a7 7 0 0 1 7 -7 Z" fill="#f7941d"/><circle cx="7" cy="7" r="2.5" fill="#3d2314"/></svg>48 Meadow Lane, Fieldton</div>
  <div style="padding-left:24px">55021, United States</div>
  <div><svg width="14" height="14" viewBox="0 0 14 14"><path d="M2 0 h3 l1 4 l-2 1 a8 8 0 0 0 5 5 l1 -2 l4 1 v3 a2 2 0 0 1 -2 2 A12 12 0 0 1 0 2 a2 2 0 0 1 2 -2 Z" fill="#f7941d"/></svg>(555) 014-2870</div>
  <div style="margin-top:10px"><svg width="16" height="12" viewBox="0 0 16 12"><rect width="16" height="12" fill="#f7941d"/><path d="M0 0 L8 7 L16 0" stroke="#3d2314" fill="none"/></svg>hello@goldensheaf-mail.com</div>
</div>

<div class="abs f-head" style="left:858px;top:3133px">Newsletter Sign Up</div>
<div class="abs news-input">Email address</div>
<a class="abs btn btn-sub" href="#">Subscribe</a>

<div class="abs copyright">© Copyright 2020 . The Golden Sheaf . All Right Reserved</div>

</body>
</html>
```